IT Services Company - Company Logo, Flyer design

We are an IT professional services company that provides technical service and support in the residential market. I would like to create a colorful logo and flyer that will be mainly letterbox dropped.

Target Market(s)

residential

Industry/Entity Type

It Company

Requirements
Must have
• nice look and feel, easy to read

```html
<!DOCTYPE html>
<html lang="en">
<head>
<meta charset="utf-8">
<title>IT Services Flyer</title>
<link rel="stylesheet" href="https://fonts.googleapis.com/css2?family=Anton&family=Montserrat:wght@400;600;700&display=swap">
<style>
  :root {
    --page-bg: #f4f4f4;
    --paper: #ffffff;
    --brand-red: #f11a0c;
    --brand-red-deep: #c90d05;
    --navy-band: #16213f;
    --headline-navy: #1a2a6c;
    --body-ink: #1d1d1d;
    --accent-yellow: #f6ff1a;
    --photo-window: #eef2f8;
    --photo-light: #c9d5ea;
    --photo-mid: #8fa3c6;
    --photo-dark: #34466e;
  }
  * { margin: 0; padding: 0; box-sizing: border-box; }
  html, body {
    width: 1200px; height: 1200px; overflow: hidden;
    background: var(--page-bg);
  }
  .flyer {
    position: absolute; left: 201px; top: 36px;
    width: 798px; height: 1128px;
    background: var(--paper);
    overflow: hidden;
  }
  .flyer__art { position: absolute; inset: 0; }
  .price-badge {
    position: absolute; left: 30px; top: 428px;
    width: 244px; height: 244px; border-radius: 50%;
    background: var(--paper);
    display: flex; align-items: center; justify-content: center;
  }
  .price-badge__disc {
    width: 230px; height: 230px; border-radius: 50%;
    background: radial-gradient(circle at 50% 45%, #ff2a14 0%, var(--brand-red) 60%, var(--brand-red-deep) 100%);
    display: flex; flex-direction: column; align-items: center; justify-content: center;
    font-family: "Anton", sans-serif; text-align: center;
  }
  .price-badge__lead { color: var(--accent-yellow); font-size: 33px; line-height: 1; }
  .price-badge__amount { color: #fff; font-size: 86px; line-height: 1.05; margin: 4px 0 2px; }
  .price-badge__note { color: var(--accent-yellow); font-size: 23px; line-height: 1; }
  .cards-note {
    position: absolute; left: 521px; top: 466px;
    font-family: "Anton", sans-serif; color: #fff;
    font-size: 52px; line-height: 68px;
  }
  .intro {
    position: absolute; left: 16px; top: 692px; width: 780px;
    font-family: "Montserrat", sans-serif; font-weight: 700;
    color: var(--headline-navy); font-size: 25.9px; line-height: 29.5px;
  }
  .services {
    position: absolute; left: 14px; top: 797px; width: 784px;
    font-family: "Montserrat", sans-serif; font-weight: 400;
    color: var(--body-ink); font-size: 19.7px; line-height: 24.7px;
    white-space: nowrap;
  }
  .procure {
    position: absolute; left: 14px; top: 1006px; width: 784px;
    font-family: "Montserrat", sans-serif; font-weight: 700;
    color: #111; font-size: 19.6px; line-height: 22px;
    white-space: nowrap;
  }
  .contact-band {
    position: absolute; left: 0; top: 1035px; width: 798px; height: 93px;
    background: linear-gradient(100deg, var(--brand-red-deep) 0%, var(--brand-red) 40%, #ff2b18 70%, var(--brand-red-deep) 100%);
    display: flex; align-items: center; justify-content: center;
    font-family: "Montserrat", sans-serif; font-weight: 700;
    color: #fff; font-size: 19.6px; line-height: 25.5px; text-align: center;
    white-space: nowrap;
  }
</style>
</head>
<body>
<main class="flyer">
  <svg class="flyer__art" width="798" height="1128" viewBox="0 0 798 1128">
    <defs>
      <linearGradient id="meetingPhoto" x1="0" y1="0" x2="0.8" y2="1">
        <stop offset="0" stop-color="var(--photo-window)"/>
        <stop offset="0.35" stop-color="var(--photo-light)"/>
        <stop offset="0.7" stop-color="var(--photo-mid)"/>
        <stop offset="1" stop-color="var(--photo-dark)"/>
      </linearGradient>
      <linearGradient id="terminalPhoto" x1="0" y1="0" x2="1" y2="1">
        <stop offset="0" stop-color="#b9bcc4"/>
        <stop offset="0.5" stop-color="#7f848f"/>
        <stop offset="1" stop-color="#4d525c"/>
      </linearGradient>
      <radialGradient id="badgeShadow" cx="0.5" cy="0.5" r="0.5">
        <stop offset="0" stop-color="#000" stop-opacity="0.45"/>
        <stop offset="1" stop-color="#000" stop-opacity="0"/>
      </radialGradient>
    </defs>
    <rect class="top-bar" x="0" y="0" width="798" height="12" fill="var(--brand-red)"/>
    <polygon class="meeting-photo" role="img" aria-label="Photo of a presenter speaking to colleagues around a table in a bright, windowed office meeting room"
             points="0,12 798,12 798,392 0,519" fill="url(#meetingPhoto)"/>
    <polygon class="navy-band" points="0,519 798,392 798,737 0,612" fill="var(--navy-band)"/>
    <line x1="259" y1="477" x2="798" y2="392" stroke="var(--brand-red)" stroke-width="5"/>
    <polygon class="red-underline" points="230,646 798,732 798,742 230,652" fill="var(--brand-red)"/>
    <ellipse cx="152" cy="668" rx="95" ry="8" fill="url(#badgeShadow)"/>
    <rect class="terminal-photo" role="img" aria-label="Photo of a card payment terminal with keypad and screen"
          x="305" y="475" width="190" height="200" rx="22" fill="url(#terminalPhoto)"
          transform="rotate(-14 400 575)"/>
  </svg>

  <div class="price-badge">
    <div class="price-badge__disc">
      <span class="price-badge__lead">We charge</span>
      <span class="price-badge__amount">$70</span>
      <span class="price-badge__note">Ex GST per hour</span>
    </div>
  </div>

  <p class="cards-note">All major<br>credit cards<br>accepted</p>

  <h1 class="intro">We are an IT professional services<br>company that provides technical service<br>andsupport&nbsp; for the North Shore residential market.</h1>

  <p class="services">StreamCast installations and wireless setup –Stream movies and shows to<br>your existing TV Computer Setup New computer recommendations New<br>computer unpacking and setup Mobile phone setups and trainingComputer<br>training Telephony &amp;Network Cable relations and installations Home Network<br>&amp; Wireless setup Improvements for extending your home Wireless IP Camera<br>installations external and internal Backup solutions either at home or to a<br>cloud provider Computer &amp; Network Security Email setup Domain setup and<br>email migration to cloud</p>

  <p class="procure">We can procure all new hardware and provide you obligation free quotes.</p>

  <footer class="contact-band">
    <p>No job is too small, please call or email our team who will be happy<br>to assist withyour&nbsp; enquiry and schedule an appointment. We<br>can also accommodate afterhours&nbsp; appointments.</p>
  </footer>
</main>
</body>
</html>
```